Brochure Design Project

We are a consulting engineering company and need to have our current company brochure updated and made to look a lot more professional.

We provide design and documentation of electrical, lighting, mechanical, hydraulic, fire, services to architects, interior designers, building owners and managers.

We are launching an updated website shortly and want a print brochure to send to clients.

Attached is our current brochure for reference.
Updates

The recent projects section should be renamed to "Completed Projects". Space should be allowed for 8 projects. I have uploaded 7 of these images and a new image will follow shortly.

We would like to include an image for each of our company services. I have uploaded 9 new images:

1. Electrical
2. Mechanical
3. Communications
4. Fire
5. Security
6. Lighting
7. Hydraulics
8. Computer Suite
9. Building Assessments

Target Market(s)

Architects, Interior Designers, Consultants, Professionals

Industry/Entity Type

Building

Requirements
Must have
• Very professional look
Simple and easy to read layout
Similar look and feel to our new website which is soon to be launched : http://www.sitehaven.co.uk/rkm/
Examples of our recent projects - around 6 projects with 1 or 2 photos per project. Will upload these soon.
A3 size, double sided with centre fold
Should not have
• Bright colours
Any comics or similar

```html
<!DOCTYPE html>
<html lang="en">
<head>
<meta charset="utf-8">
<title>RKM Consulting Services – Brochure</title>
<link href="https://fonts.googleapis.com/css2?family=Arimo:ital,wght@0,400;0,700;1,700&display=swap" rel="stylesheet">
<style>
  :root{
    --stage:#d9d6d0;
    --cover-top:#5a5a5a;
    --cover-mid:#7a7a7a;
    --quote-band:#6e6e6e;
    --quote-mark:#4f4f4f;
    --logo-band:#c9c9c9;
    --band-dark:#1f2322;
    --band-sheen:#4a504e;
    --page:#e6e6e6;
    --text:#3a3a3a;
    --heading:#222;
    --photo-a:#8e8a86;
    --photo-b:#c9c6c1;
  }
  *{box-sizing:border-box;margin:0;padding:0}
  html,body{width:1200px;height:900px;overflow:hidden}
  body{background:var(--stage);font-family:"Arimo",Arial,sans-serif;color:var(--text);position:relative}

  .cover,.spread{position:absolute;top:210px;height:480px;box-shadow:0 8px 24px rgba(0,0,0,.25)}
  .cover{left:70px;width:340px;display:flex;flex-direction:column}
  .cover__art{flex:0 0 282px;background:linear-gradient(160deg,var(--cover-top),var(--cover-mid) 55%,#8a8a8a)}
  .cover__quote{flex:0 0 104px;background:var(--quote-band);color:#fff;font-weight:700;font-style:italic;font-size:14px;line-height:1.3;padding:14px 32px 0 58px;position:relative}
  .cover__quote::before{content:"\201C";position:absolute;left:22px;top:4px;font-size:44px;line-height:1;color:var(--quote-mark)}
  .cover__quote::after{content:"\201D";position:absolute;right:12px;bottom:-14px;font-size:44px;line-height:1;color:var(--quote-mark)}
  .cover__brand{flex:1;background:linear-gradient(180deg,#d6d6d6,var(--logo-band));display:flex;align-items:center;justify-content:center;gap:8px}
  .brand__mark{width:12px;height:12px;background:var(--band-dark)}
  .brand__name{font-size:12px;letter-spacing:2px;color:#2a2a2a;font-weight:400}

  .spread{left:450px;width:680px;display:flex;flex-direction:column}
  .spread__band{background:linear-gradient(180deg,var(--band-dark),var(--band-sheen) 50%,var(--band-dark))}
  .spread__band--top{flex:0 0 40px}
  .spread__band--bottom{flex:0 0 55px}
  .spread__body{flex:1;background:var(--page);display:flex;position:relative}
  .spread__body::after{content:"";position:absolute;left:338px;top:0;bottom:0;width:4px;background:linear-gradient(90deg,rgba(0,0,0,.05),rgba(0,0,0,.18),rgba(0,0,0,.05))}
  .page{width:340px;display:flex;gap:12px;padding:8px 0}
  .page--left{padding-right:14px}
  .page--right{padding-left:18px}
  .photos{width:130px;display:flex;flex-direction:column;gap:8px}
  .photo{flex:1;background:linear-gradient(135deg,var(--photo-a),var(--photo-b))}
  .services{flex:1;display:flex;flex-direction:column;gap:4px;padding-top:4px}
  .service h3{font-size:7.5px;font-weight:700;color:var(--heading);margin-bottom:1px}
  .service li{list-style:none;font-size:6.6px;line-height:8.4px}
</style>
</head>
<body>

<section class="cover">
  <div class="cover__art" role="img" aria-label="Faint grey montage of rolled architectural plans"></div>
  <blockquote class="cover__quote">Every project receives a level of dedication, commitment and service to ensure client expectations are exceeded</blockquote>
  <div class="cover__brand"><span class="brand__mark"></span><span class="brand__name">RKM Consulting Services Pty Ltd</span></div>
</section>

<section class="spread">
  <div class="spread__band spread__band--top"></div>
  <div class="spread__body">
    <div class="page page--left">
      <div class="photos">
        <div class="photo" role="img" aria-label="Boardroom with brick wall and black chairs"></div>
        <div class="photo" role="img" aria-label="Meeting room with white table and tall windows"></div>
        <div class="photo" role="img" aria-label="Open plan office with workstations"></div>
      </div>
      <div class="services">
        <div class="service"><h3>Electrical Services</h3><ul>
          <li>Power distribution</li><li>General lighting</li><li>Feature lighting for highlight/contrast</li><li>of client orientated areas</li><li>Programmable lighting control</li><li>Emergency lighting and exit signs</li><li>Electrical consumption management</li><li>Lighting control integration with</li><li>energy management systems</li><li>Evacuation warning systems</li><li>Power conditioners</li><li>Public address installations</li><li>Television signal distribution</li></ul></div>
        <div class="service"><h3>Critical Use Installations</h3><ul>
          <li>Layout and space allowance</li><li>for hardware and equipment</li><li>Uninterruptable power supplies</li><li>and power conditioning</li><li>Access control and intruder detection</li><li>Fire rating</li><li>Anti static solutions</li><li>PABX and VOIP integration</li><li>Dedicated electrical distribution systems</li><li>Standby power supplies</li><li>High heat rejection cooling solutions</li></ul></div>
        <div class="service"><h3>Computer Suite Audits</h3><ul>
          <li>Comprehensive Computer Suite Audits</li><li>Australian Standard Compliance</li><li>TIA 942 Tier Rating certification</li></ul></div>
        <div class="service"><h3>Hydraulic Services</h3><ul>
          <li>Water supplies</li><li>Waste discharge</li><li>Venting</li><li>Water heating and cooling</li><li>Filtration</li></ul></div>
        <div class="service"><h3>Fire Services</h3><ul>
          <li>Electronic Smoke and Thermal Detection</li><li>Aspirating Detection Systems</li><li>Fire Suppression Systems</li><li>Fire Sprinkler Systems</li></ul></div>
      </div>
    </div>
    <div class="page page--right">
      <div class="services">
        <div class="service"><h3>Communication Systems</h3><ul>
          <li>Telephone cabling</li><li>Data cabling</li><li>Patch field configurations</li><li>Fibre optic distribution systems</li><li>Integration of voice and</li><li>data cabling systems</li><li>Verification testing</li><li>Compliance with relevant codes</li><li>and installation practices</li><li>LAN Cable distribution systems</li></ul></div>
        <div class="service"><h3>Security Services</h3><ul>
          <li>Electronic access control</li><li>Integration of existing systems</li><li>with client requirements</li><li>Intruder detection</li><li>Off site monitoring and alarms</li><li>CCTV</li></ul></div>
        <div class="service"><h3>Mechanical Services</h3><ul>
          <li>Direct Cooling System</li><li>Air and Water Cooled Chilled Water System</li><li>BMS and DDC Control System</li><li>Computer and Data Centre Solutions</li><li>Ducted Water and Air</li><li>Cooled System (Single or</li><li>Multiple Indoor Units)</li><li>VAV and Chilled Beams</li><li>Industrial and Commercial</li><li>Humidification</li><li>Commercial and Industrial Evaporative</li><li>Cooling Using Air Washers</li></ul></div>
        <div class="service"><h3>Building Assessment</h3><ul>
          <li>Building services condition assessment</li><li>Advise relative to available building services</li><li>(for long or short term purposes)</li><li>Trouble Shooting and Investigation</li><li>Review of Existing Systems</li><li>Upgrade for Current and Future Refurbishment</li></ul></div>
      </div>
      <div class="photos">
        <div class="photo" role="img" aria-label="Long boardroom with brick wall and windows"></div>
        <div class="photo" role="img" aria-label="Training room with projection screen"></div>
        <div class="photo" role="img" aria-label="Open plan office with white desks"></div>
      </div>
    </div>
  </div>
  <div class="spread__band spread__band--bottom"></div>
</section>

</body>
</html>
```